Packaging Design Project - Organic Baby Skin Care

This project is to re-design our current organic baby skin care range labels. See here:

http://www.velvetmeadow.com.au/Baby-Care

The common complaint is that the pink is too girly for boys. For this reason I am not sure if I should keep the "Velvet Meadow Baby" Logo as it is a bit girly looking as well. So open to your ideas.

The size of the label will be approx 90 w x 70 h mm

Here is one range I like that is already similar to what I am already doing with the polka dots but in different pastels: http://www.tinkettlestore.com/baby-skincare.html

Also another idea for a concept here with a beige/vintage look background: http://www.barnloftstore.com/wee_lark_naturals/wee_lark_naturals_creamy_body_lotion-c502817p730461.html

Lastly, I also like these fun colourful, child like graphics of this range:

http://www.tinyfernnaturals.co.uk/brands/hush-drowsy-bean/

The range consists of:

Soothing Tot Salve in a white tube
Bubbly Fresh Tot Wash in a white 250ml bottle
Nana and Pip Rubdown Oil in a white 100ml bottle
Quiet Night Settling Spray in a white 100ml bottle
Oat Cream Bar in a cardboard box

See packaging attached.

I will be presenting all the designs to a group of mother's for market research so they will be making the final decision - seeing they are the ones who will ultimately buy the product.

That is why I am open to a wide range of styles for this project.

Looking forward to seeing your work!

Any questions, let me know!
Updates

Hello Designers!

I have posted an update to include more information in the brief and also the AI logo file which shows the current packaging. Also images of the bottles of the current range. The bottles will be white boston round bottles not the tall boston as I am currently using.

many thanks

Rosalind

Hello Designers

Just wanted to get an update on how you are going with your design submissions?

The deadline is this Saturday and we have received very few designs.

I await your reply.

thanks
Rosalind

Reason: The deadline is drawing near and have not received enough designs. Please submit your designs as soon as you can. Many thanks Rosalind Velvet Meadow

Target Market(s)

Mothers 25 - 40

Industry/Entity Type

Market Research

Requirements
Must have
• Organic/Natural feel, Stylish, Elegant, Gender Neutral to suit both sexes
Nice to have
• Vintage feel

```html
<!DOCTYPE html>
<html lang="en">
<head>
<meta charset="utf-8">
<title>Velvet Meadow Baby – Label Range</title>
<link rel="stylesheet" href="https://fonts.googleapis.com/css2?family=Cormorant+Garamond:wght@400;500;600&display=swap">
<style>
  :root {
    --lilac: #c6a6da;
    --lilac-line: #b996cf;
    --lilac-text: #a47fbd;
    --stripe: #f2eaf3;
    --cream: #fcfaf0;
    --lime: #c5d62a;
    --lime-text: #b6c81c;
    --page: #ffffff;
  }
  * { box-sizing: border-box; margin: 0; padding: 0; }
  html, body { width: 1200px; height: 763px; overflow: hidden; background: var(--page); }
  body { font-family: "Cormorant Garamond", serif; }

  .range {
    width: 1200px; height: 763px;
    display: flex; align-items: center; justify-content: center; gap: 28px;
  }
  .label {
    width: 206px; height: 340px; padding: 12px;
    background: repeating-linear-gradient(180deg, var(--stripe) 0 34px, var(--cream) 34px 68px);
  }
  .label--wash { width: 226px; height: 372px; }
  .label__frame {
    height: 100%;
    border: 2px solid var(--lilac-line); border-radius: 26px;
    display: flex; flex-direction: column; align-items: center;
    padding: 16px 10px 12px; text-align: center;
  }
  .brand {
    color: var(--lilac-text); font-weight: 600; font-size: 21px; line-height: 1.05;
  }
  .artwork {
    width: 100%; height: 108px; margin: 8px 0 6px; border-radius: 8px;
    background: linear-gradient(135deg, var(--lime) 0%, #dcc8e8 45%, var(--lilac) 70%, var(--lime) 100%);
  }
  .label--wash .artwork { height: 124px; }
  .product {
    color: var(--lilac-text); font-weight: 500; font-size: 19px; line-height: 1.12;
  }
  .french {
    color: var(--lilac-text); font-size: 10.5px; line-height: 1.25; margin-top: 10px;
  }
  .claims {
    color: var(--lime-text); font-weight: 500; font-size: 11px; line-height: 1.3; margin-top: 8px;
  }
  .size {
    color: var(--lilac-text); font-weight: 600; font-size: 10.5px; margin-top: auto;
  }
</style>
</head>
<body>
<main class="range">

  <section class="label label--soap">
    <div class="label__frame">
      <p class="brand">Velvet Meadow<br>Baby</p>
      <div class="artwork" role="img" aria-label="Lilac bird perched on a leafy lime green branch"></div>
      <h2 class="product">Organic<br>Oat Cream Bar</h2>
      <p class="claims">Contains certified organic ingredients<br>fragrance free</p>
      <p class="size">℮ 100 g &nbsp;3.5 fl oz.</p>
    </div>
  </section>

  <section class="label label--salve">
    <div class="label__frame">
      <p class="brand">Velvet Meadow<br>Baby</p>
      <div class="artwork" role="img" aria-label="Lilac bird perched on a leafy lime green branch"></div>
      <h2 class="product">Soothing Tot<br>Salve</h2>
      <p class="french">Baume Curatif Pour Bébé</p>
      <p class="claims">Organic Herbal Blend<br>Shalphate &amp; Paraben Free</p>
      <p class="size">℮ 100 g &nbsp;3.5 fl oz.</p>
    </div>
  </section>

  <section class="label label--wash">
    <div class="label__frame">
      <p class="brand">Velvet Meadow<br>Baby</p>
      <div class="artwork" role="img" aria-label="Lilac bird perched on a leafy lime green branch"></div>
      <h2 class="product">Bubbly Fresh<br>Tot Wash</h2>
      <p class="french">Savon Pour Le Bain De Bebe</p>
      <p class="claims">Organic Herbal Blend<br>Shalphate &amp; Paraben Free</p>
      <p class="size">℮ 250ml &nbsp;8.5fl oz.</p>
    </div>
  </section>

  <section class="label label--oil">
    <div class="label__frame">
      <p class="brand">Velvet Meadow<br>Baby</p>
      <div class="artwork" role="img" aria-label="Lilac bird perched on a leafy lime green branch"></div>
      <h2 class="product">Nana &amp; Pip<br>Rubdown Oil</h2>
      <p class="french">Huile de Massage<br>Pour Maman et Bébé</p>
      <p class="claims">Organic Herbal Blend<br>Shalphate &amp; Paraben Free</p>
      <p class="size">℮ 100g &nbsp;3.5fl oz.</p>
    </div>
  </section>

  <section class="label label--spray">
    <div class="label__frame">
      <p class="brand">Velvet Meadow<br>Baby</p>
      <div class="artwork" role="img" aria-label="Lilac bird perched on a leafy lime green branch"></div>
      <h2 class="product">Quiet Night<br>Settling Spray</h2>
      <p class="french">Huile de Massage<br>Pour Maman et Bébé</p>
      <p class="claims">Organic Herbal Blend<br>Shalphate &amp; Paraben Free</p>
      <p class="size">℮ 250ml &nbsp;8.5fl oz.</p>
    </div>
  </section>

</main>
</body>
</html>
```